Flyer für Restaurant
Zielgruppe
Deutsche Küche mit Südafrikanischen Flair
Restaurant was auch Feierlichkeiten anbieten
Jung und Alt
Aufgabenstellung
Farbe : Wein rot und grau
Erleben Sie bei uns einen Abend mit vielfältiger oder deutscher Küche und all ihren Rafinessen. Sehen Sie sich unser Restaurant Gasthaus Dornbeck an, das mit einer Vielzahl an schmackhaften Speisen begeistert und noch dazu urgemütlich ist. Absolute Erholung bietet an warmen Tagen unser toller Außenbereich.
Parken können Sie ganz einfach vor dem Restaurant auf unseren kostenlosen Parkplätzen. Uns ist es wichtig, dass wir alle Menschen willkommen heißen können. Aus diesem Grund haben wir einen barrierefreien Zugang. Gerne nehmen wir Ihre Reservierung entgegen. Freuen Sie sich auf einen wundervollen Aufenthalt mit idyllischem Flair in unserem Restaurant. Darüber hinaus können Sie uns einfach per Telefon unter +4957218640 kontaktieren.
Flyer um in Briefkasten zu werfen

```html
<!DOCTYPE html>
<html lang="de">
<head>
<meta charset="utf-8">
<title>Gasthaus Dornbeck – Flyer</title>
<link href="https://fonts.googleapis.com/css2?family=Roboto+Slab:wght@300;400&family=Roboto:wght@300;400;700&family=UnifrakturMaguntia&display=swap" rel="stylesheet">
<style>
  :root{
    --wine-top:#93304a;
    --wine:#86203a;
    --wine-deep:#741028;
    --grey:#a3a3a6;
    --grey-light:#e7e7e8;
    --white:#ffffff;
    --text-soft:#f1d9de;
    --pin:#e0434f;
  }
  *{box-sizing:border-box;margin:0;padding:0}
  html,body{width:1200px;height:1200px;overflow:hidden;background:var(--grey-light)}
  .flyer{
    position:absolute;left:190px;top:20px;width:820px;height:1160px;
    background:linear-gradient(180deg,var(--wine-top) 0%,var(--wine) 40%,var(--wine-deep) 100%);
    overflow:hidden;color:var(--white);
    font-family:'Roboto',sans-serif;
    box-shadow:0 10px 30px rgba(0,0,0,.15);
  }
  .phone-pill{
    position:absolute;right:0;top:70px;height:64px;padding:0 60px 0 40px;
    background:var(--white);border-radius:32px 0 0 32px;
    color:var(--wine);font:700 34px 'Roboto',sans-serif;letter-spacing:1px;
    display:flex;align-items:center;
  }
  .brand{position:absolute;left:60px;top:100px;display:flex;align-items:center;gap:16px}
  .brand-mark{width:16px;height:16px;border:2px solid var(--white);border-radius:50%}
  .brand-name{font:400 22px 'Roboto Slab',serif;color:var(--white);line-height:1.1}
  .divider{position:absolute;left:408px;top:112px;width:2px;height:26px;background:var(--white);opacity:.8}
  .gallery{position:absolute;left:60px;top:190px;width:700px;height:230px}
  .photo{position:absolute;top:0;width:220px;height:210px;box-shadow:0 6px 14px rgba(0,0,0,.3)}
  .photo.table{background:linear-gradient(160deg,#b8a58a,#d9cfc2 45%,#6f7650 75%,#c9bba5)}
  .photo.house{background:linear-gradient(180deg,#7c95b8 0%,#e4dccb 35%,#c9bfa9 65%,#4c4b47 100%)}
  .photo .curl{position:absolute;right:0;bottom:0;width:44px;height:44px;background:linear-gradient(135deg,transparent 50%,#fff 50%)}
  .pin{position:absolute;width:20px;height:20px;border-radius:50%;background:var(--pin);top:-10px;left:-10px;box-shadow:0 2px 3px rgba(0,0,0,.3)}
  .headline{position:absolute;left:60px;top:448px;width:700px;font:400 40px/1.15 'Roboto Slab',serif}
  .headline .name{font-family:'UnifrakturMaguntia',cursive;font-size:46px}
  .intro{position:absolute;left:60px;top:568px;width:680px;font:300 17px/1.45 'Roboto',sans-serif;color:var(--text-soft)}
  .intro p+p{margin-top:16px}
  .grey-band{position:absolute;left:330px;top:728px;width:490px;height:30px;background:linear-gradient(90deg,rgba(163,163,166,0),var(--grey) 70%)}
  .comfort-title{position:absolute;left:160px;top:772px;font:400 28px/1.2 'Roboto Slab',serif}
  .timeline{position:absolute;left:0;top:0;width:820px;height:1160px}
  .features{position:absolute;left:175px;top:830px;width:600px;list-style:none;font:300 16px/1.4 'Roboto',sans-serif;color:var(--text-soft)}
  .features li{margin-bottom:14px}
  .features b{font-weight:700;color:var(--white)}
  .reserve{position:absolute;left:175px;top:1004px;width:600px}
  .reserve h2{font:400 38px/1.2 'Roboto Slab',serif;margin-bottom:10px}
  .reserve p{font:300 15px/1.5 'Roboto',sans-serif;color:var(--text-soft)}
  .reserve p strong{font-weight:700;color:var(--white)}
</style>
</head>
<body>
<main class="flyer">
  <div class="phone-pill">+4957218640</div>

  <div class="brand">
    <span class="brand-mark"></span>
    <span class="brand-name">Gasthaus Dornbeck</span>
  </div>
  <span class="divider"></span>

  <section class="gallery">
    <div class="photo table" style="left:20px;top:20px" role="img" aria-label="Festlich gedeckter Tisch mit Eukalyptus-Gesteck und Kerzen"><span class="pin"></span><span class="curl"></span></div>
    <div class="photo house" style="left:250px" role="img" aria-label="Fassade des Gasthauses mit Terrasse und Sonnenschirm"><span class="pin"></span><span class="curl"></span></div>
    <div class="photo table" style="left:480px;top:-10px" role="img" aria-label="Tischdekoration mit grünem Gesteck im Gastraum"><span class="pin"></span><span class="curl"></span></div>
  </section>

  <h1 class="headline">Ein Abend deutscher Vornehmheit im<br><span class="name">Gasthaus Dornbeck</span></h1>

  <div class="intro">
    <p>Erleben Sie einen unvergesslichen Abend mit uns und genießen Sie die Vielfalt der deutschen Küche in all ihren Facetten.</p>
    <p>Besuchen Sie unser Restaurant Gasthaus Dornbeck, das Sie mit einer Auswahl an köstlichen Gerichten verwöhnt und sich dabei wunderbar gemütlich verwöhnen lässt. Wir bieten Ihnen einen traumhaften Aufenthalt mit idyllischem Flair.</p>
  </div>

  <div class="grey-band"></div>
  <h3 class="comfort-title">Ihr Komfort ist unsere Priorität.</h3>

  <svg class="timeline" viewBox="0 0 820 1160" aria-hidden="true">
    <defs>
      <linearGradient id="accent" x1="0" x2="1"><stop offset="0" stop-color="#e0434f"/><stop offset="1" stop-color="#741028" stop-opacity="0"/></linearGradient>
    </defs>
    <rect x="60" y="779" width="80" height="22" fill="url(#accent)"/>
    <path d="M130 810 V960 Q130 990 160 990 H760 Q790 990 790 1020 V1160" fill="none" stroke="#fff" stroke-width="2"/>
    <path d="M540 812 H770 Q790 812 790 832 V990" fill="none" stroke="#fff" stroke-width="2" opacity=".9"/>
    <circle cx="130" cy="790" r="20" fill="#fff"/>
    <path d="M123 797 h14 l-2-3 v-6 a5 5 0 0 0-10 0 v6 z M128 799 h4 a2 2 0 0 1-4 0z" fill="#86203a"/>
    <circle cx="130" cy="842" r="9" fill="#86203a" stroke="#fff" stroke-width="2"/>
    <circle cx="130" cy="900" r="9" fill="#86203a" stroke="#fff" stroke-width="2"/>
    <circle cx="130" cy="936" r="9" fill="#86203a" stroke="#fff" stroke-width="2"/>
  </svg>

  <ul class="features">
    <li><b>Entspannte Atmosphäre:</b> An warmen Tagen lädt unser großzügiger Außenbereich zum Verweilen und Entspannen ein.</li>
    <li><b>Barrierefreier Zugang:</b> Wir heißen alle Gäste herzlich willkommen.</li>
    <li><b>Bequemes Parken:</b> Parken Sie bequem auf unseren kostenlosen Parkplätzen direkt vor dem Restaurant.</li>
  </ul>

  <section class="reserve">
    <h2>Reservieren Sie Ihren Tisch</h2>
    <p>Wir freuen uns auf Ihre Reservierung! Freuen Sie sich auf ein perfektes kulinarisches Erlebnis, bei dem Qualität, Komfort und Gastfreundschaft aufeinandertreffen.<br><strong>Sie erreichen uns ganz einfach telefonisch unter +4957218640.</strong></p>
  </section>
</main>
</body>
</html>
```